New Business Card Design Project

I would like to purchase a customized version of a design you have previously submitted - https://www.plomarket.com/design/7724163<br/><br/>I would like to incorporate the attached Images for my fitness company "TalvrenPro Athletics". My initial services is personal training and athletic performance. I would like a card that has one a shiny black side with the silver logo and the side with a white background utilizing the gold logo. On the white side, put "Sports Performance and Functional Strength Training" under the logo.
Industry/Entity Type
Fitness
Contact Information for Business Card
Marcus Tolley
Owner and Trainer
555.273.8492
marcus.tolley@talvrenproathletics.com
Look and feel
Each slider illustrates characteristics of the customer's brand and the style your logo design should communicate.

```html
<!DOCTYPE html>
<html lang="en">
<head>
<meta charset="utf-8">
<title>TalvrenPro Athletics – Business Card</title>
<link rel="stylesheet" href="https://fonts.googleapis.com/css2?family=Poppins:wght@300;400;500&family=Russo+One&display=swap">
<style>
  :root {
    --stage: #e7e4df;
    --black: #0e0e0e;
    --black-soft: #1d1d1d;
    --silver: #d6d6d6;
    --gold: #9c8450;
    --gold-light: #c2aa74;
    --white: #ffffff;
    --ink: #151515;
    --grey-text: #8a8a8a;
  }
  * { margin: 0; padding: 0; box-sizing: border-box; }
  html, body { width: 1200px; height: 900px; overflow: hidden; }
  body {
    background: var(--stage);
    font-family: "Poppins", Arial, sans-serif;
    position: relative;
  }
  .card {
    position: absolute;
    left: 250px;
    width: 700px;
    height: 400px;
    overflow: hidden;
    box-shadow: 0 12px 30px rgba(0,0,0,0.22);
  }
  /* Black side */
  .card-back {
    top: 35px;
    background: linear-gradient(135deg, var(--black-soft) 0%, var(--black) 55%, #050505 100%);
  }
  .card-back .faint-ring {
    position: absolute;
    right: -60px; top: 170px;
    width: 330px; height: 330px;
    border-radius: 50%;
    border: 26px solid rgba(255,255,255,0.035);
  }
  .brand-mark {
    position: absolute;
    display: flex;
    align-items: center;
    gap: 14px;
    font-weight: 500;
    letter-spacing: 3px;
    text-transform: uppercase;
    white-space: nowrap;
  }
  .brand-mark .dot {
    border-radius: 50%;
    flex: none;
  }
  .card-back .brand-mark {
    left: 50%; top: 120px;
    transform: translateX(-50%);
    color: var(--silver);
    font-size: 28px;
  }
  .card-back .brand-mark .dot {
    width: 46px; height: 46px;
    background: var(--silver);
  }
  .tagline {
    position: absolute;
    text-transform: uppercase;
    white-space: nowrap;
  }
  .card-back .tagline {
    left: 0; right: 0; top: 250px;
    text-align: center;
    color: var(--silver);
    font-size: 15px;
    letter-spacing: 2.5px;
  }
  /* White side */
  .card-front {
    top: 465px;
    background: var(--white);
  }
  .card-front .brand-mark {
    left: 40px; top: 38px;
    color: var(--gold);
    font-size: 24px;
  }
  .card-front .brand-mark .dot {
    width: 40px; height: 40px;
    background: var(--gold);
  }
  .card-front .tagline {
    left: 40px; top: 92px;
    color: var(--grey-text);
    font-size: 12px;
    letter-spacing: 2px;
  }
  .card-front .faint-ring {
    position: absolute;
    right: -40px; top: 120px;
    width: 300px; height: 300px;
    border-radius: 50%;
    border: 22px solid rgba(0,0,0,0.035);
  }
  .contact-block {
    position: absolute;
    left: 250px; top: 140px;
  }
  .person-name {
    font-family: "Russo One", Arial, sans-serif;
    font-weight: 400;
    font-size: 30px;
    color: var(--ink);
    line-height: 1.1;
  }
  .person-role {
    font-weight: 300;
    font-size: 19px;
    color: var(--grey-text);
    margin-bottom: 16px;
  }
  .contact-list { list-style: none; }
  .contact-list li {
    display: flex;
    align-items: center;
    gap: 12px;
    font-weight: 300;
    font-size: 17px;
    color: #555;
    line-height: 30px;
    white-space: nowrap;
  }
  .contact-list svg { width: 16px; height: 16px; flex: none; fill: var(--gold); }
  .base-band {
    position: absolute;
    left: 0; right: 0; bottom: 0;
    height: 34px;
    background: linear-gradient(180deg, #2a2a2a, var(--black));
    border-top: 3px solid var(--gold-light);
  }
</style>
</head>
<body>
  <section class="card card-back" aria-label="Card back">
    <div class="faint-ring"></div>
    <div class="brand-mark"><span class="dot"></span>TalvrenPro Athletics</div>
    <p class="tagline">Sports Performance and Functional Training</p>
  </section>

  <section class="card card-front" aria-label="Card front">
    <div class="faint-ring"></div>
    <div class="brand-mark"><span class="dot"></span>TalvrenPro Athletics</div>
    <p class="tagline">Sports Performance and Functional Strength Training</p>
    <div class="contact-block">
      <h1 class="person-name">Marcus Tolley</h1>
      <p class="person-role">Owner and Trainer</p>
      <ul class="contact-list">
        <li><svg viewBox="0 0 24 24"><path d="M6.6 10.8a15.1 15.1 0 0 0 6.6 6.6l2.2-2.2a1 1 0 0 1 1-.25 11.4 11.4 0 0 0 3.6.57 1 1 0 0 1 1 1V20a1 1 0 0 1-1 1A17 17 0 0 1 3 4a1 1 0 0 1 1-1h3.5a1 1 0 0 1 1 1c0 1.25.2 2.45.57 3.57a1 1 0 0 1-.25 1z"/></svg>555.273.8492</li>
        <li><svg viewBox="0 0 24 24"><path d="M2 5h20v14H2z M2 5l10 8 10-8" fill="none" stroke="#9c8450" stroke-width="2"/></svg>marcus.tolley@talvrenproathletics.com</li>
        <li><svg viewBox="0 0 24 24"><circle cx="12" cy="12" r="9" fill="none" stroke="#9c8450" stroke-width="2"/><path d="M3 12h18M12 3c3 3 3 15 0 18M12 3c-3 3-3 15 0 18" fill="none" stroke="#9c8450" stroke-width="1.6"/></svg>www.TalvrenProAthletics.com</li>
      </ul>
    </div>
    <div class="base-band"></div>
  </section>
</body>
</html>
```